Double sided customer happy holidays and thank you card

Create a simple holiday theme thank you and happy holidays card using white and red (CMYK 0.94.100.0) as the primary colors with a dash of green (CMYK 85.3.91.44) peppered in the color scheme.
1. draft for templates in portrait view using: 4x6, 5x7, 5.5x8.5, and 6x9 (templates guidelines with bleed, trim, and safe areas attached.
2. Make prominent use of the company logo and icons (attached).
3. Backside of the card is devoted to customer instructions (attached).
4. Frontside wording draft attached.
5. Signatures, Marcus & Linda, should be in handwritten script.
6. Words should be in a super large font size so that print is easy to read for all customers.

```html
<!DOCTYPE html>
<html lang="en">
<head>
<meta charset="utf-8">
<title>Crumbwell Holiday Card</title>
<link href="https://fonts.googleapis.com/css2?family=Libre+Baskerville&family=Nunito+Sans:wght@300;400&family=Great+Vibes&family=Quicksand:wght@400;500&display=swap" rel="stylesheet">
<style>
  :root {
    --red: #ed3a26;
    --red-soft: #f26a4f;
    --salmon: #f4a48a;
    --green: #0e6b3b;
    --olive: #6f7a38;
    --sage: #b9d4c3;
    --blush: #f6c3b3;
    --white: #ffffff;
    --ink: #1a1a1a;
    --line: #c9c9c9;
  }
  * { box-sizing: border-box; margin: 0; padding: 0; }
  html, body { width: 1200px; height: 1200px; overflow: hidden; background: var(--white); }
  body { position: relative; font-family: "Nunito Sans", sans-serif; }

  .side-label {
    position: absolute;
    font-family: "Libre Baskerville", serif;
    font-size: 17px;
    color: var(--ink);
  }
  .label-back { left: 165px; top: 577px; }
  .label-front { left: 1040px; top: 577px; }
  .label-inside { left: 172px; top: 1163px; }

  .sheet {
    position: absolute;
    left: 237px;
    width: 765px;
    overflow: hidden;
  }
  .sheet-outside { top: 21px; height: 573px; background: var(--red); }
  .sheet-inside { top: 610px; height: 572px; background: var(--white); border: 1px solid var(--line); }
  .fold {
    position: absolute; left: 382px; top: 0; bottom: 0; width: 1px;
    background: rgba(0,0,0,0.08);
  }

  /* Decorative areas */
  .decor { position: absolute; }
  .decor-front-top {
    left: 240px; top: 0; width: 525px; height: 250px;
    background: radial-gradient(ellipse at 55% 40%, rgba(246,170,150,0.55), rgba(237,58,38,0) 70%);
  }
  .decor-front-wreath {
    left: 400px; top: 260px; width: 300px; height: 200px;
    background: radial-gradient(ellipse at center, rgba(255,255,255,0.22), rgba(237,58,38,0) 70%);
  }
  .decor-inside-left {
    left: 0; top: 0; width: 420px; height: 572px;
    background:
      radial-gradient(circle at 27% 3%, rgba(185,212,195,0.9) 0 60px, transparent 61px),
      radial-gradient(ellipse at 40% 45%, rgba(246,195,179,0.45), transparent 55%),
      radial-gradient(ellipse at 85% 45%, rgba(185,212,195,0.5), transparent 40%),
      radial-gradient(ellipse at 50% 95%, rgba(246,195,179,0.55), transparent 45%);
  }

  /* Back panel */
  .care-title {
    position: absolute; left: 63px; top: 50px;
    font-family: "Libre Baskerville", serif;
    font-size: 19px; line-height: 24px; color: var(--white);
  }
  .care-brand {
    position: absolute; left: 63px; top: 98px;
    font-family: "Quicksand", sans-serif; font-weight: 400;
    font-size: 42px; color: var(--white); letter-spacing: 0.5px;
  }
  .care-box {
    position: absolute; left: 67px; top: 150px; width: 265px; height: 350px;
    background: var(--white); border: 1.5px solid var(--green);
  }
  .care-box-head {
    background: var(--green); color: var(--white);
    font-family: "Libre Baskerville", serif; font-size: 11.5px;
    height: 23px; line-height: 23px; text-align: center; letter-spacing: 0.3px;
  }
  .care-steps { list-style: none; padding: 15px 19px 0 28px; }
  .care-step {
    position: relative;
    font-size: 10.4px; line-height: 14px; color: var(--green);
    text-align: justify; margin-bottom: 6px;
  }
  .care-step .brand { color: var(--red); }
  .step-num {
    position: absolute; left: -44px; top: -4px;
    width: 28px; height: 28px; border-radius: 50%;
    background: var(--white); border: 1.5px dotted var(--red);
    display: flex; align-items: center; justify-content: center;
  }
  .step-num span {
    width: 15px; height: 15px; border-radius: 50%;
    background: var(--green); color: var(--white);
    font-family: "Libre Baskerville", serif; font-size: 9px;
    display: flex; align-items: center; justify-content: center;
  }
  .care-signoff {
    position: absolute; left: 67px; top: 503px;
    font-family: "Great Vibes", cursive; font-size: 21px; color: var(--white);
  }

  /* Front panel */
  .front-lockup {
    position: absolute; left: 505px; top: 468px; width: 240px;
    display: flex; flex-direction: column; align-items: center;
  }
  .front-name {
    font-family: "Quicksand", sans-serif; font-weight: 500;
    font-size: 40px; line-height: 50px; color: var(--green);
    background: var(--white); padding: 0 12px; border-radius: 10px;
  }
  .front-tagline {
    margin-top: 4px;
    font-family: "Quicksand", sans-serif; font-weight: 500;
    font-size: 12px; line-height: 20px; color: var(--green); letter-spacing: 0.6px;
    background: var(--white); padding: 0 10px; border-radius: 10px;
  }

  /* Inside greeting */
  .greeting {
    position: absolute; left: 382px; top: 0; width: 383px;
    text-align: center;
  }
  .greeting-title {
    margin-top: 62px; font-weight: 400;
    font-family: "Libre Baskerville", serif; font-size: 25px; color: var(--red);
  }
  .greeting-from {
    font-family: "Great Vibes", cursive; font-size: 22px; color: var(--red);
    margin-top: 2px;
  }
  .greeting-mark {
    width: 40px; height: 40px; margin: 4px auto 0;
    border-radius: 50%; border: 1.5px dotted var(--green);
  }
  .greeting-brand {
    font-family: "Quicksand", sans-serif; font-weight: 500;
    font-size: 42px; line-height: 48px; color: var(--green); margin-top: 4px;
  }
  .rule { width: 80px; height: 1px; background: var(--green); margin: 6px auto 4px; }
  .rule-red { background: var(--red); margin: 8px auto 8px; }
  .greeting-family { font-size: 10.5px; color: var(--green); }
  .greeting-copy {
    font-size: 12.2px; line-height: 14.5px; color: var(--red);
    margin: 0 auto; white-space: nowrap;
  }
  .copy-first { margin-top: 38px; }
  .copy-space { margin-top: 14px; }
  .greeting-cheers { font-size: 12.2px; color: var(--red); margin-top: 14px; }
  .greeting-sign {
    font-family: "Great Vibes", cursive; font-size: 30px; color: var(--green);
    margin-top: 16px;
  }
</style>
</head>
<body>

<div class="side-label label-back">back</div>
<div class="side-label label-front">front</div>
<div class="side-label label-inside">inside</div>

<section class="sheet sheet-outside">
  <div class="decor decor-front-top" role="img" aria-label="Scattered pattern of dashed bundt cake rings and garlands in white, salmon and olive"></div>
  <div class="decor decor-front-wreath" role="img" aria-label="Wreath of dotted cake ring icons in white and green"></div>
  <div class="fold"></div>

  <div class="care-title">Getting the<br>most out of your</div>
  <div class="care-brand">crumbwell</div>

  <div class="care-box">
    <div class="care-box-head">CARE, STORAGE, AND ENJOYMENT</div>
    <ol class="care-steps">
      <li class="care-step"><div class="step-num"><span>1</span></div>Prepare to rekindle your love for pound cake again for the first time, or simply prepare for a love-at-first-bite pound cake experience with your <span class="brand">crumbwell</span>.</li>
      <li class="care-step"><div class="step-num"><span>2</span></div>Remember, in order to maintain the quality and freshness of your <span class="brand">crumbwell</span>, please store it in an airtight container and keep it in a cool, dry place for up to five days.</li>
      <li class="care-step"><div class="step-num"><span>3</span></div>You can also save your <span class="brand">crumbwell</span> for later enjoyment after 5 days. To begin with, wrap in food-grade plastic wrap. Next, cover with aluminum foil. Then freeze for up to four months. However, if you prefer, you can pre-slice before wrapping and freezing and then store the slices in a freezer storage bag for later slice-by-slice enjoyment.</li>
      <li class="care-step"><div class="step-num"><span>4</span></div>When ready for another moment of enjoyment, remove your <span class="brand">crumbwell</span> from the freezer, let it thaw at room temperature, then unwrap and serve.</li>
    </ol>
  </div>

  <div class="care-signoff">Enjoy your moments by the pound!</div>

  <div class="front-lockup">
    <div class="front-name">crumbwell</div>
    <div class="front-tagline">a pound cakery</div>
  </div>
</section>

<section class="sheet sheet-inside">
  <div class="decor decor-inside-left" role="img" aria-label="Soft pattern of dotted cake rings and dashed garlands in blush pink and sage"></div>
  <div class="fold"></div>

  <div class="greeting">
    <h1 class="greeting-title">Happy Holidays</h1>
    <div class="greeting-from">from the</div>
    <div class="greeting-mark"></div>
    <div class="greeting-brand">crumbwell</div>
    <div class="rule"></div>
    <div class="greeting-family">pound cakery family!</div>

    <p class="greeting-copy copy-first">We are thankful for the<br>opportunity to be a VIP at your<br>table this holiday season -<br>although not for long, we’re sure!</p>
    <div class="rule rule-red"></div>
    <p class="greeting-copy">Thanks for allowing us to be a part of<br>your moments this year and this holiday<br>season. We are in your debt.</p>
    <p class="greeting-copy copy-space">May we be the first to wish you Happy<br>Holidays and Happy New Year!</p>
    <p class="greeting-cheers">Cheers by the pound!</p>
    <div class="greeting-sign">Marcus &amp; Linda</div>
  </div>
</section>

</body>
</html>
```